Tirovel

We need a business card for our company is a holding for different business all are different we try to have some air of relax and fun in our projects we add pictures of the office to give you an idea od the mood of the business

Business

```html
<!DOCTYPE html>
<html lang="en">
<head>
<meta charset="UTF-8">
<title>Tirovel — Business Card</title>
<link href="https://fonts.googleapis.com/css2?family=Arimo:wght@400;700&display=swap" rel="stylesheet">
<style>
  :root {
    --backdrop: #d9d9d9;
    --card-brown: #613a0b;
    --brand-yellow: #f4e51c;
    --text-white: #ffffff;
  }
  * { margin: 0; padding: 0; box-sizing: border-box; }
  html, body {
    width: 1200px;
    height: 800px;
    overflow: hidden;
    background: var(--backdrop);
    font-family: "Arimo", Arial, sans-serif;
  }
  .business-card {
    position: absolute;
    left: 180px;
    top: 160px;
    width: 840px;
    height: 480px;
    background: var(--card-brown);
  }
  .brand-block {
    position: absolute;
    left: 300px;
    top: 0;
    width: 270px;
    height: 262px;
    background: var(--brand-yellow);
    display: flex;
    align-items: center;
    justify-content: center;
  }
  .brand-name {
    font-weight: 700;
    font-size: 66px;
    line-height: 1;
    letter-spacing: -2px;
    color: var(--card-brown);
  }
  .holder-name {
    position: absolute;
    left: 300px;
    top: 284px;
    width: 270px;
    text-align: center;
    font-weight: 700;
    font-size: 24px;
    color: var(--brand-yellow);
  }
  .contact-row {
    position: absolute;
    left: 0;
    top: 356px;
    width: 100%;
    display: flex;
    justify-content: center;
    gap: 36px;
    color: var(--text-white);
    font-size: 24px;
  }
  .contact-item {
    display: flex;
    align-items: center;
    gap: 10px;
  }
  .contact-icon { width: 22px; height: 22px; }
</style>
</head>
<body>
  <div class="business-card">
    <div class="brand-block">
      <span class="brand-name">Tirovel</span>
    </div>
    <p class="holder-name">Name Here</p>
    <div class="contact-row">
      <div class="contact-item">
        <svg class="contact-icon" viewBox="0 0 22 22" aria-hidden="true">
          <circle cx="11" cy="11" r="10" fill="var(--text-white)"/>
          <path d="M8 6 L10 6 L10.6 8.6 L9.4 9.6 Q10.4 12 12.6 13 L13.6 11.8 L16 12.4 L16 14.4 Q12 15.8 9 12.6 Q6.4 9.6 8 6 Z" fill="var(--card-brown)"/>
        </svg>
        <span class="contact-text">+00 585 8888 99</span>
      </div>
      <div class="contact-item">
        <svg class="contact-icon" viewBox="0 0 22 22" aria-hidden="true">
          <circle cx="11" cy="11" r="9.5" fill="none" stroke="var(--text-white)" stroke-width="2"/>
          <rect x="6" y="7.5" width="10" height="7" fill="none" stroke="var(--text-white)" stroke-width="1.5"/>
          <path d="M6 7.5 L11 11.5 L16 7.5" fill="none" stroke="var(--text-white)" stroke-width="1.5"/>
        </svg>
        <span class="contact-text">xxxx@xxxxxxx.com</span>
      </div>
    </div>
  </div>
</body>
</html>
```